*WRAP* Car dealer needs cool wrap design for commercial VAN

We need a wrap design for our commercial vehicle (BRAXO DELIVO LINK 2015). We are a company that buys and sells cars and originated from offering pre-purchase inspections. We want to radiate that we are a modern, reliable, honest company with a little exclusivity.

Looking at options for a full wrap and half wrap.

Target Market(s)

age 20-50

Industry/Entity Type

Automotive

Font styles to use
Other font styles liked:
• Audiowide regular, Yellowtail

Requirements
Must have
• Please include the address, Phone number, logo and the text: Occasions | Aankoopkeuringen (meaning; second hand cars & pre-purchase inspections).

Information can be found here: www.verdaan-motorhuis.nl
Nice to have
• We would like to see the following colors reflected in the design:

Yellow: RGB (242, 195, 20)
Gray: RGB (68, 68, 68)

Preferably with (part of) the banner image from our website www.verdaan-motorhuis.nl incorporated in the design, for example on the side or at the back.

```html
<!DOCTYPE html>
<html lang="en">
<head>
<meta charset="utf-8">
<title>Verdaan Motorhuis – Van Wrap</title>
<link rel="stylesheet" href="https://fonts.googleapis.com/css2?family=Audiowide&family=Quicksand:wght@600;700&display=swap">
<style>
  :root {
    --brand-yellow: #f2c314;
    --brand-gray: #444444;
    --body-dark: #3a3a3a;
    --glass: #dfe3e4;
    --white: #ffffff;
    --tyre: #1e1e1e;
    --rim: #c9ccce;
    --canvas: #ffffff;
  }
  html, body {
    margin: 0;
    padding: 0;
    width: 1200px;
    height: 884px;
    overflow: hidden;
    background: var(--canvas);
  }
  .wrap-canvas { display: block; width: 1200px; height: 884px; }
  .brand-name { font-family: "Audiowide", sans-serif; fill: var(--white); }
  .service-line { font-family: "Quicksand", sans-serif; font-weight: 700; fill: var(--white); font-size: 15px; letter-spacing: 0.5px; }
  .contact-label { font-family: "Quicksand", sans-serif; font-weight: 700; fill: var(--brand-gray); font-size: 14px; }
  .contact-phone { font-family: "Quicksand", sans-serif; font-weight: 700; fill: var(--white); font-size: 22px; }
  .web-address { font-family: "Quicksand", sans-serif; font-weight: 700; fill: var(--white); font-size: 14px; letter-spacing: 0.6px; }
  .social-dot { fill: none; stroke: var(--brand-gray); stroke-width: 1.4; }
</style>
</head>
<body>
<svg class="wrap-canvas" viewBox="0 0 1200 884" xmlns="http://www.w3.org/2000/svg">
  <defs>
    <clipPath id="van-body">
      <path d="M200,250 Q210,242 240,241 L560,240 Q640,242 700,268 L840,380 Q900,385 1000,410 Q1055,425 1062,450 L1068,545 L1060,575 L985,575 A70,70 0 0 0 845,575 L395,575 A70,70 0 0 0 255,575 L160,575 L150,555 L165,420 Q170,300 200,250 Z"/>
    </clipPath>
    <linearGradient id="field-tones" x1="0" y1="0" x2="1" y2="1">
      <stop offset="0" stop-color="#d9a64a"/>
      <stop offset="0.35" stop-color="#b8893a"/>
      <stop offset="0.7" stop-color="#c9953b"/>
      <stop offset="1" stop-color="#8a6a34"/>
    </linearGradient>
    <linearGradient id="front-fade" x1="0" y1="0" x2="1" y2="0">
      <stop offset="0" stop-color="#ffffff" stop-opacity="0"/>
      <stop offset="0.35" stop-color="#ffffff"/>
      <stop offset="1" stop-color="#ffffff"/>
    </linearGradient>
    <linearGradient id="car-tones" x1="0" y1="0" x2="1" y2="1">
      <stop offset="0" stop-color="#6f8fb0"/>
      <stop offset="0.5" stop-color="#7a4a3c"/>
      <stop offset="1" stop-color="#b98a55"/>
    </linearGradient>
  </defs>

  <!-- antenna -->
  <line x1="655" y1="203" x2="700" y2="265" stroke="var(--brand-gray)" stroke-width="2"/>

  <g class="van-panel" clip-path="url(#van-body)">
    <rect x="140" y="230" width="940" height="360" fill="var(--body-dark)"/>
    <rect class="landscape-photo" role="img" aria-label="Sunlit golden grass field with hills, the company website banner photo"
          x="150" y="240" width="680" height="320" fill="url(#field-tones)" opacity="0.92"/>
    <polygon points="340,240 700,240 700,268 560,300" fill="var(--body-dark)"/>
    <rect x="780" y="360" width="300" height="230" fill="url(#front-fade)"/>
    <polygon points="575,452 672,427 855,490 815,540 760,540" fill="var(--brand-yellow)"/>
    <polygon points="380,490 465,558 380,558" fill="var(--brand-yellow)"/>
    <rect x="150" y="555" width="930" height="30" fill="var(--tyre)"/>
  </g>

  <!-- window -->
  <path d="M578,282 L700,288 L790,360 L790,402 L625,398 Z" fill="var(--glass)" stroke="var(--brand-gray)" stroke-width="6"/>
  <rect x="425" y="505" width="360" height="30" rx="10" fill="#333" opacity="0.85"/>

  <!-- service band with its text -->
  <g class="service-band" transform="translate(392,382) rotate(20)">
    <rect x="0" y="0" width="330" height="28" fill="var(--brand-gray)"/>
    <text class="service-line" x="18" y="19" textLength="292">Occasions  |  Purchase inspections</text>
  </g>

  <line x1="567" y1="270" x2="567" y2="575" stroke="#2a2a2a" stroke-width="1.5"/>

  <!-- lens ring with photo -->
  <circle cx="305" cy="425" r="92" fill="var(--brand-gray)" stroke="var(--white)" stroke-width="2"/>
  <circle class="car-photo" role="img" aria-label="Close-up photo of a dark red car door and mirror"
          cx="305" cy="425" r="65" fill="url(#car-tones)" stroke="var(--white)" stroke-width="2"/>

  <!-- brand -->
  <g class="brand-mark" transform="rotate(22 300 275)">
    <circle cx="282" cy="270" r="20" fill="var(--brand-yellow)"/>
    <text class="brand-name" x="312" y="285" font-size="38">VERDAAN</text>
    <text class="brand-name" x="340" y="322" font-size="26">MOTORHUIS</text>
  </g>

  <!-- contact block -->
  <g class="contact-block" transform="translate(660,440) rotate(20)">
    <text class="contact-label" x="6" y="0">Contact us:</text>
    <text class="contact-phone" x="-24" y="25">+316 4817 3920</text>
  </g>

  <text class="web-address" x="495" y="553">www.verdaan-motorhuis.nl</text>

  <g class="social-links">
    <circle class="social-dot" cx="880" cy="435" r="11"/>
    <circle class="social-dot" cx="910" cy="435" r="11"/>
    <circle class="social-dot" cx="941" cy="435" r="11"/>
  </g>

  <!-- headlight -->
  <path d="M985,415 Q1035,425 1052,440 L1048,452 Q1010,446 995,432 Z" fill="var(--body-dark)"/>

  <!-- wheels -->
  <g class="wheel">
    <circle cx="318" cy="560" r="68" fill="var(--tyre)"/>
    <circle cx="318" cy="560" r="46" fill="var(--rim)"/>
    <circle cx="318" cy="560" r="8" fill="var(--brand-gray)"/>
  </g>
  <g class="wheel">
    <circle cx="910" cy="560" r="68" fill="var(--tyre)"/>
    <circle cx="910" cy="560" r="46" fill="var(--rim)"/>
    <circle cx="910" cy="560" r="8" fill="var(--brand-gray)"/>
  </g>
</svg>
</body>
</html>
```